Morvela Aesthetic Doctor

I require an elegant, luxurious looking business card for my aesthetic business. I am a doctor and that will set me aside from competitors. I am planning to provide home and spa based treatments to clients with high expectations. I have attached my logo.

```html
<!DOCTYPE html>
<html lang="en">
<head>
<meta charset="utf-8">
<title>Morvela Aesthetic Doctor – Business Card</title>
<link href="https://fonts.googleapis.com/css2?family=Roboto:wght@300;400;500&display=swap" rel="stylesheet">
<style>
  :root {
    --page: #e4e4e4;
    --card-front: #ffffff;
    --card-back: #a7a9ab;
    --sky: #5bbde8;
    --sky-deep: #2f8fd0;
    --ink: #8c8e91;
    --ink-soft: #9a9c9f;
    --white: #ffffff;
    --mist: #e6eef8;
  }
  * { box-sizing: border-box; margin: 0; padding: 0; }
  html, body {
    width: 1125px; height: 1200px; overflow: hidden;
    background: var(--page);
    font-family: "Roboto", Arial, sans-serif;
  }
  .canvas { position: relative; width: 1125px; height: 1200px; }
  .card {
    position: absolute; left: 150px; width: 825px; height: 470px;
    border-radius: 24px; overflow: hidden;
    box-shadow: 0 3px 6px rgba(0,0,0,.25);
  }
  .card--front { top: 98px; background: var(--card-front); }
  .card--back { top: 632px; background: var(--card-back); }

  .decor {
    position: absolute; border-radius: 50%;
  }
  .card--front .decor {
    left: 330px; top: 0; width: 470px; height: 470px;
    background: radial-gradient(circle at 55% 45%, rgba(200,218,240,.55), rgba(230,238,248,.25) 60%, rgba(255,255,255,0) 72%);
  }
  .card--back .decor {
    left: 320px; top: 10px; width: 470px; height: 450px;
    background: radial-gradient(circle at 55% 50%, rgba(190,192,195,.7), rgba(175,177,180,.3) 60%, rgba(167,169,171,0) 72%);
  }

  .wordmark { position: absolute; font-weight: 300; line-height: 1; }
  .wordmark__name { display: block; letter-spacing: 2px; }
  .wordmark__tag { display: block; letter-spacing: 1.5px; margin-top: 8px; }

  .card--front .wordmark { left: 52px; top: 44px; color: var(--ink); }
  .card--front .wordmark__name { font-size: 54px; }
  .card--front .wordmark__tag { font-size: 23px; }

  .card--back .wordmark { left: 360px; top: 140px; color: var(--white); }
  .card--back .wordmark__name { font-size: 62px; }
  .card--back .wordmark__tag { font-size: 28px; }

  .brand-mark {
    position: absolute; left: 150px; top: 128px; width: 180px; height: 150px;
    border-radius: 50%;
    background: radial-gradient(circle at 45% 45%, var(--sky-deep), var(--sky) 55%, rgba(91,189,232,0) 75%);
  }

  .holder { position: absolute; left: 52px; top: 248px; }
  .holder__name { font-size: 29px; font-weight: 500; color: var(--sky); }
  .holder__post { font-size: 18px; font-weight: 400; letter-spacing: .5px; }
  .holder__title { margin-top: 6px; font-size: 21px; font-weight: 300; color: var(--ink-soft); }

  .contact { position: absolute; left: 52px; top: 332px; list-style: none; }
  .contact__item {
    display: flex; align-items: center; height: 33px;
    font-size: 21px; font-weight: 300; color: var(--ink-soft);
  }
  .contact__item svg { width: 18px; height: 18px; margin-right: 14px; }
  .contact__accent { color: var(--sky); }

  .social { position: absolute; left: 306px; top: 397px; display: flex; gap: 20px; }
  .social__dot { width: 26px; height: 26px; border-radius: 50%; background: var(--sky); }

  .services {
    position: absolute; left: 0; right: 0; top: 316px;
    text-align: center; color: var(--white);
    font-size: 21px; font-weight: 300; line-height: 33px;
  }
  .services__sep { font-size: 14px; vertical-align: 2px; padding: 0 4px; }
</style>
</head>
<body>
<main class="canvas">

  <section class="card card--front">
    <div class="decor" role="img" aria-label="Faint brand emblem decoration"></div>
    <div class="wordmark">
      <span class="wordmark__name">MORVELA</span>
      <span class="wordmark__tag">AESTHETIC DOCTOR</span>
    </div>
    <div class="holder">
      <p class="holder__name">Dr Elin Varga, <span class="holder__post">MRCPCH MD</span></p>
      <p class="holder__title">Australasian Diploma of Aesthetic Medicine</p>
    </div>
    <ul class="contact">
      <li class="contact__item">
        <svg viewBox="0 0 24 24"><path fill="#5bbde8" d="M6.6 10.8a15.2 15.2 0 0 0 6.6 6.6l2.2-2.2a1 1 0 0 1 1-.25 11.4 11.4 0 0 0 3.6.57 1 1 0 0 1 1 1V20a1 1 0 0 1-1 1A17 17 0 0 1 3 4a1 1 0 0 1 1-1h3.5a1 1 0 0 1 1 1c0 1.25.2 2.45.57 3.57a1 1 0 0 1-.25 1z"/></svg>
        0800 414 737
      </li>
      <li class="contact__item">
        <svg viewBox="0 0 24 24"><rect x="3" y="5" width="18" height="14" rx="1.5" fill="none" stroke="#5bbde8" stroke-width="2"/><path d="M3.5 6l8.5 7 8.5-7" fill="none" stroke="#5bbde8" stroke-width="2"/></svg>
        elin@morvela.co.nz
      </li>
      <li class="contact__item">
        <svg viewBox="0 0 24 24" fill="none" stroke="#5bbde8" stroke-width="1.6"><circle cx="12" cy="12" r="9"/><ellipse cx="12" cy="12" rx="4" ry="9"/><path d="M3 12h18M4.5 7.5h15M4.5 16.5h15"/></svg>
        www.<span class="contact__accent">morvela</span>.co.nz
      </li>
    </ul>
    <div class="social">
      <span class="social__dot"></span>
      <span class="social__dot"></span>
    </div>
  </section>

  <section class="card card--back">
    <div class="decor" role="img" aria-label="Faint brand emblem decoration"></div>
    <div class="brand-mark" role="img" aria-label="Brand emblem"></div>
    <div class="wordmark">
      <span class="wordmark__name">MORVELA</span>
      <span class="wordmark__tag">AESTHETIC DOCTOR</span>
    </div>
    <div class="services">
      <p>Dermal injectables <span class="services__sep">●</span> Plasma facials <span class="services__sep">●</span> Microneedling</p>
      <p>Skin boosters <span class="services__sep">●</span> Excessive sweating</p>
      <p>Home and Spa Based Treatments</p>
    </div>
  </section>

</main>
</body>
</html>
```